Verpackungsetikett für Softeisbecher
Zielgruppe
Wir produzieren Speiseeis, füllen dieses in entsprechende Verpackungseinheiten ab und vermarkten es. Zielgruppe sind alle die, die Eis mögen.
Aufgabenstellung
Das bestehende Etikettendesign (rund 8cm Durchmesser) soll neu überarbeitet werden. Dazu soll es mit unserem neuen Logo (Anhang) versehen werden. Wir freuen uns über fotolose Vorschläge bzw. Design´s mit Foto. Alle Angaben über z.B. Inhaltstoffe, Herstellungdatum, Aufbewahrungtemperatur, Barcode u.s.w.kommen auf ein separates Etikett am Boden des Bechers.Das Erscheinungsbild des Etiketts sollte eine gewisse Neutralität haben, so dass es für die verschiedensten Geschmacksrichtungen verwendet werden kann, sprich ein Etikett für alle Eissorten. Nur der Name der Geschmacksrichtung unterscheidet die Etiketten. Wir verweisen auf einige Link`s ,auf denen man Etikettenbeispiele (z. B. Frischkäse) sieht, die unseren Vorstellungen der Gestaltung entsprechen. Vielen Dank im Voraus

```html
<!DOCTYPE html>
<html lang="de">
<head>
<meta charset="utf-8">
<title>Speise-Eis Etiketten</title>
<link rel="stylesheet" href="https://fonts.googleapis.com/css2?family=Rammetto+One&family=Nunito:wght@800;900&family=Kaushan+Script&display=swap">
<style>
  :root {
    --bg: #ffffff;
    --navy: #1b3a8a;
    --navy-dark: #12296a;
    --sky: #6fa6da;
    --sky-light: #c9def2;
    --ice: #eef5fc;
    --lime: #9bbb2a;
    --berry-ring: #ee8a8c;
    --berry-ring-light: #f7c2c2;
    --berry-tag: #b8231f;
    --vanilla-ring: #f8ecaa;
    --vanilla-ring-light: #fdf7d6;
    --vanilla-tag: #fbf1b8;
    --ink: #2a1a12;
    --white: #ffffff;
  }
  html, body {
    margin: 0;
    width: 1200px;
    height: 722px;
    overflow: hidden;
    background: var(--bg);
  }
  .sheet { position: relative; width: 1200px; height: 722px; }
  .label { position: absolute; top: 118px; width: 480px; height: 480px; }
  .label--strawberry { left: 105px; }
  .label--vanilla { left: 652px; }
  .ribbon-text {
    font-family: "Nunito", sans-serif; font-weight: 800; font-size: 19px; fill: var(--white);
  }
  .brand-name {
    font-family: "Nunito", sans-serif; font-weight: 900; font-size: 30px; fill: var(--lime);
  }
  .product-name {
    font-family: "Rammetto One", serif; font-size: 50px; fill: var(--navy);
    stroke: var(--white); stroke-width: 9px; paint-order: stroke; stroke-linejoin: round;
  }
  .product-name__tilde { font-size: 30px; }
  .flavour-name { font-family: "Kaushan Script", cursive; font-size: 30px; }
  .flavour-name--strawberry { fill: var(--white); }
  .flavour-name--vanilla { fill: var(--ink); }
</style>
</head>
<body>
<main class="sheet">

  <svg class="label label--strawberry" viewBox="0 0 480 480" aria-label="Etikett Erdbeere">
    <defs>
      <clipPath id="s-outer"><circle cx="240" cy="240" r="240"/></clipPath>
      <clipPath id="s-inner"><circle cx="240" cy="242" r="222"/></clipPath>
      <linearGradient id="s-ring" x1="0" y1="0" x2="0" y2="1">
        <stop offset="0.4" stop-color="var(--berry-ring-light)"/>
        <stop offset="1" stop-color="var(--berry-ring)"/>
      </linearGradient>
      <linearGradient id="s-top" x1="0" y1="0" x2="1" y2="0">
        <stop offset="0" stop-color="var(--navy-dark)"/>
        <stop offset="0.55" stop-color="var(--navy)"/>
        <stop offset="1" stop-color="var(--sky)"/>
      </linearGradient>
      <linearGradient id="s-face" x1="0" y1="0" x2="0" y2="1">
        <stop offset="0" stop-color="var(--sky-light)"/>
        <stop offset="0.35" stop-color="var(--white)"/>
        <stop offset="1" stop-color="var(--ice)"/>
      </linearGradient>
      <linearGradient id="s-deep" x1="0" y1="0" x2="0" y2="1">
        <stop offset="0" stop-color="var(--sky-light)"/>
        <stop offset="0.4" stop-color="var(--sky)"/>
        <stop offset="1" stop-color="var(--sky-light)"/>
      </linearGradient>
      <radialGradient id="s-fruit" cx="0.4" cy="0.4" r="0.6">
        <stop offset="0" stop-color="#f0483c"/>
        <stop offset="1" stop-color="#b3161a"/>
      </radialGradient>
    </defs>
    <g clip-path="url(#s-outer)">
      <rect class="ring" width="480" height="480" fill="url(#s-ring)"/>
      <path class="ring-top" d="M0 0 H480 V195 C360 185 160 190 0 225 Z" fill="url(#s-top)"/>
    </g>
    <g clip-path="url(#s-inner)">
      <rect x="0" y="0" width="480" height="480" fill="url(#s-face)"/>
      <path class="wave wave--white" d="M0 120 C120 60 300 130 480 70 V40 C300 90 140 20 0 80 Z" fill="var(--white)" opacity="0.8"/>
      <path class="wave wave--deep" d="M0 285 C150 255 320 300 480 260 V480 H0 Z" fill="url(#s-deep)"/>
      <path class="wave wave--white" d="M0 300 C160 270 330 300 480 250 V270 C330 320 160 290 0 315 Z" fill="var(--white)" opacity="0.75"/>
    </g>
    <g clip-path="url(#s-outer)">
      <polygon class="ribbon" points="-48,191 242,-60 278,-20 -12,231" fill="var(--lime)"/>
      <text class="ribbon-text" x="0" y="7" text-anchor="middle" transform="translate(118 92) rotate(-41)">Natürlich lecker!</text>
    </g>
    <text class="brand-name" x="240" y="188" text-anchor="middle">mirelvo</text>
    <text class="product-name" x="240" y="262" text-anchor="middle">Speise<tspan class="product-name__tilde" dy="-12">~</tspan><tspan dy="12">Eis</tspan></text>
    <path class="flavour-tag" d="M88 334 L258 320 L264 376 L94 390 Z" fill="var(--berry-tag)"/>
    <text class="flavour-name flavour-name--strawberry" x="166" y="366" text-anchor="middle" transform="rotate(-4 166 366)">Erdbeere</text>
    <ellipse class="flavour-picture" role="img" aria-label="Illustration einer Erdbeere mit grünen Blättern" cx="298" cy="355" rx="57" ry="68" fill="url(#s-fruit)"/>
  </svg>

  <svg class="label label--vanilla" viewBox="0 0 480 480" aria-label="Etikett Vanille">
    <defs>
      <clipPath id="v-outer"><circle cx="240" cy="240" r="240"/></clipPath>
      <clipPath id="v-inner"><circle cx="240" cy="242" r="222"/></clipPath>
      <linearGradient id="v-ring" x1="0" y1="0" x2="0" y2="1">
        <stop offset="0.4" stop-color="var(--vanilla-ring-light)"/>
        <stop offset="1" stop-color="var(--vanilla-ring)"/>
      </linearGradient>
      <linearGradient id="v-top" x1="0" y1="0" x2="1" y2="0">
        <stop offset="0" stop-color="var(--navy-dark)"/>
        <stop offset="0.55" stop-color="var(--navy)"/>
        <stop offset="1" stop-color="var(--sky)"/>
      </linearGradient>
      <linearGradient id="v-face" x1="0" y1="0" x2="0" y2="1">
        <stop offset="0" stop-color="var(--sky-light)"/>
        <stop offset="0.35" stop-color="var(--white)"/>
        <stop offset="1" stop-color="var(--ice)"/>
      </linearGradient>
      <linearGradient id="v-deep" x1="0" y1="0" x2="0" y2="1">
        <stop offset="0" stop-color="var(--sky-light)"/>
        <stop offset="0.4" stop-color="var(--sky)"/>
        <stop offset="1" stop-color="var(--sky-light)"/>
      </linearGradient>
      <linearGradient id="v-pod" x1="0" y1="0" x2="1" y2="1">
        <stop offset="0" stop-color="#fbf3c4"/>
        <stop offset="0.55" stop-color="#efe2a0"/>
        <stop offset="1" stop-color="#4a3022"/>
      </linearGradient>
    </defs>
    <g clip-path="url(#v-outer)">
      <rect class="ring" width="480" height="480" fill="url(#v-ring)"/>
      <path class="ring-top" d="M0 0 H480 V195 C360 185 160 190 0 225 Z" fill="url(#v-top)"/>
    </g>
    <g clip-path="url(#v-inner)">
      <rect x="0" y="0" width="480" height="480" fill="url(#v-face)"/>
      <path class="wave wave--white" d="M0 120 C120 60 300 130 480 70 V40 C300 90 140 20 0 80 Z" fill="var(--white)" opacity="0.8"/>
      <path class="wave wave--deep" d="M0 285 C150 255 320 300 480 260 V480 H0 Z" fill="url(#v-deep)"/>
      <path class="wave wave--white" d="M0 300 C160 270 330 300 480 250 V270 C330 320 160 290 0 315 Z" fill="var(--white)" opacity="0.75"/>
    </g>
    <g clip-path="url(#v-outer)">
      <polygon class="ribbon" points="-48,191 242,-60 278,-20 -12,231" fill="var(--lime)"/>
      <text class="ribbon-text" x="0" y="7" text-anchor="middle" transform="translate(118 92) rotate(-41)">Natürlich lecker!</text>
    </g>
    <text class="brand-name" x="240" y="188" text-anchor="middle">mirelvo</text>
    <text class="product-name" x="240" y="262" text-anchor="middle">Speise<tspan class="product-name__tilde" dy="-12">~</tspan><tspan dy="12">Eis</tspan></text>
    <path class="flavour-tag" d="M116 334 L272 320 L278 374 L122 388 Z" fill="var(--vanilla-tag)"/>
    <text class="flavour-name flavour-name--vanilla" x="196" y="366" text-anchor="middle" transform="rotate(-4 196 366)">Vanille</text>
    <path class="flavour-picture" role="img" aria-label="Illustration einer Vanilleblüte mit Vanilleschoten" d="M270 305 C305 290 350 300 360 330 C368 360 345 385 320 385 L200 410 C186 410 184 398 198 392 L262 372 C250 350 248 318 270 305 Z" fill="url(#v-pod)"/>
  </svg>

</main>
</body>
</html>
```